Book Cover design - Education & Research

We need a design of the book cover for a book written in an education sector. It has been written by a professor with target audience being other professors, lecturers, PhD students etc. The book is about Singapore's development as a country (from third world to economical leader) with high emphasis on it's education sector. It explores many education concepts that could set an example for other countries.
We would like the design to be serious, modern, representing innovation, progress in the educations space. The colours will be mainly red and white representing the country's flag. Probably white background with red additions. The design will consist of three parts:
1) Front cover (the most important where the designer should put most effort in). At the top will be name of the author: Zofia Kradecka, below name of the book: "Odlegle Sciezki Nauczania" with smaller subtitle below: "Zielone Mosty Pomiedzy Szkolami Zielone Mosty Pomiedzy Szkolami"
2) Back cover (very simple with majority of the space put for text, reviews etc.)
3) Second page already inside the book (less important, just a simple black and white design in this part)
We welcome any creative designs from your part, but for reference below is an idea of how we would like it to look like. I would recommend for the designers to do two designs. One according to the below instructions and another with your own idea how to go about it. Please do keep in mind that we can't use proprietary Singapore icons like quorvex or exact design of Singapore flag, so please don't use these.
Our idea:
- The front page to have cityscape with silhouettes of Singapore iconic buildings (Coral Hill Towers, Halvern Wheel, Lumen Craft Gallery, Corvanta, Terraces of Wrenfield, Sky scrappers)
- A red and white ribbon starting at the front and then going through the spine of the book to the back cover.
NOTE:
- We would like to see more designs with your own creativity and other colors, not only red and white
Education sector, Universities, Professors

```html
<!DOCTYPE html>
<html lang="pl">
<head>
<meta charset="utf-8">
<title>Odlegle Sciezki Nauczania – okladka</title>
<link rel="stylesheet" href="https://fonts.googleapis.com/css2?family=Archivo+Black&family=Oswald:wght@500;600&family=Poppins:wght@300;400&family=Roboto:wght@400&family=Roboto+Condensed:ital,wght@0,500;1,700&display=swap">
<style>
  :root{
    --page:#ffffff;
    --ink:#111111;
    --ink-soft:#1c1c1c;
    --grey-text:#6a6a6a;
    --spine-blue:#1b8fd6;
    --navy:#0d2a66;
    --band-1:#dfe3ea;
    --band-2:#eef0f4;
    --band-3:#c9d0dc;
    --city-sky:#b9cde3;
    --city-mid:#5a7fa6;
    --city-lights:#d8b76a;
    --water:#c7d2e0;
    --skyline:#c8d0da;
    --shadow:rgba(0,0,0,.35);
  }
  *{box-sizing:border-box;margin:0;padding:0}
  html,body{width:1200px;height:612px;overflow:hidden;background:var(--page)}
  .canvas{position:relative;width:1200px;height:612px;background:var(--page)}

  .cover-wrap{position:absolute;left:51px;top:50px;width:748px;height:508px;background:var(--page);overflow:hidden;box-shadow:0 4px 14px var(--shadow)}
  .inner-page{position:absolute;left:814px;top:49px;width:346px;height:509px;background:var(--page);overflow:hidden;box-shadow:0 4px 14px var(--shadow)}

  .wrap-art{position:absolute;inset:0}

  .back-bio{position:absolute;left:20px;top:66px;width:158px;text-align:right;font-family:"Roboto",sans-serif;font-size:9.2px;line-height:11.35px;color:var(--ink-soft)}
  .back-bio .bio-name{font-size:10.5px}
  .author-portrait{position:absolute;left:184px;top:68px;width:131px;height:156px;background:linear-gradient(160deg,#2a2a2a,#050505)}

  .back-blurb{position:absolute;left:28px;width:290px;font-family:"Roboto",sans-serif;font-size:5.9px;line-height:7.82px;letter-spacing:.15px;color:var(--ink);white-space:nowrap}
  .back-blurb.first{top:236px}
  .back-blurb.second{top:348px}

  .spine-text{position:absolute;left:365px;writing-mode:vertical-rl;font-family:"Archivo Black",sans-serif;font-size:15px;letter-spacing:1px;white-space:nowrap}
  .spine-author{top:34px;color:var(--spine-blue)}
  .spine-title{top:199px;color:var(--ink)}

  .front-author{position:absolute;left:440px;width:300px;top:42px;text-align:center;font-family:"Poppins",sans-serif;font-weight:300;font-size:19px;letter-spacing:5px;color:var(--ink)}
  .front-title{position:absolute;left:420px;width:320px;top:222px;text-align:center;font-family:"Archivo Black",sans-serif;font-size:27px;line-height:45px;letter-spacing:2.5px;color:#fff;text-shadow:2px 2px 3px rgba(0,0,0,.75)}
  .front-subtitle{position:absolute;left:420px;width:320px;top:310px;text-align:center;font-family:"Roboto Condensed",sans-serif;font-style:italic;font-weight:700;font-size:10.5px;letter-spacing:.4px;color:var(--ink);white-space:nowrap}

  .inner-author{position:absolute;left:0;width:100%;top:58px;text-align:center;font-family:"Poppins",sans-serif;font-weight:400;font-size:18px;letter-spacing:4px;color:var(--ink)}
  .inner-title{position:absolute;left:0;width:100%;top:214px;text-align:center;font-family:"Oswald",sans-serif;font-weight:600;font-size:20px;letter-spacing:1.6px;color:var(--ink)}
  .inner-subtitle{position:absolute;left:0;width:100%;top:283px;text-align:center;font-family:"Roboto Condensed",sans-serif;font-weight:500;font-size:18.5px;line-height:27px;letter-spacing:1.4px;color:var(--grey-text)}
  .inner-skyline{position:absolute;left:0;bottom:0;width:100%;height:100px}
</style>
</head>
<body>
<main class="canvas">

  <section class="cover-wrap" aria-label="Okladka: tyl, grzbiet i przod">
    <svg class="wrap-art" viewBox="0 0 748 508" width="748" height="508" aria-hidden="false">
      <defs>
        <linearGradient id="cityGlow" x1="0" y1="0" x2="0" y2="1">
          <stop offset="0" stop-color="var(--city-sky)"/>
          <stop offset=".45" stop-color="var(--city-mid)"/>
          <stop offset=".62" stop-color="var(--city-lights)" stop-opacity=".8"/>
          <stop offset=".78" stop-color="var(--city-mid)"/>
          <stop offset="1" stop-color="var(--water)"/>
        </linearGradient>
        <linearGradient id="bandFade" x1="0" y1="0" x2="1" y2="1">
          <stop offset="0" stop-color="var(--band-3)"/>
          <stop offset="1" stop-color="var(--band-2)"/>
        </linearGradient>
      </defs>
      <polygon class="band" points="36,0 140,0 410,508 340,508" fill="url(#bandFade)" opacity=".75"/>
      <polygon class="band" points="140,0 150,0 420,508 410,508" fill="var(--band-3)"/>
      <polygon class="band" points="220,0 360,0 748,300 748,410" fill="var(--band-2)" opacity=".9"/>
      <polygon class="band" points="430,0 560,0 748,110 748,180" fill="var(--band-1)" opacity=".6"/>
      <polygon class="band" points="380,508 748,180 748,230 450,508" fill="var(--band-1)" opacity=".7"/>
      <polygon class="city-photo" role="img" aria-label="Nocna panorama miasta nad zatoka z wiezowcami i szklarniami ogrodow" points="340,508 748,128 748,508" fill="url(#cityGlow)"/>
      <line class="accent-line" x1="600" y1="250" x2="748" y2="124" stroke="var(--navy)" stroke-width="2.2"/>
      <line class="accent-line" x1="660" y1="285" x2="748" y2="232" stroke="var(--ink)" stroke-width="1.6"/>
    </svg>

    <div class="back-bio">
      <span class="bio-name">Zofia Kradecka</span> about the author<br>
      lorem ipsum lorem ipsum lorem ipsum<br>
      lorem ipsum lorem ipsum lorem ipsum<br>
      lorem ipsum lorem ipsum lorem ipsum<br>
      lorem ipsum lorem ipsum lorem ipsum<br>
      lorem ipsum lorem ipsum lorem ipsum<br>
      lorem ipsum lorem ipsum lorem ipsum<br>
      lorem ipsum lorem ipsum<br>
      lorem ipsum lorem ipsum<br>
      lorem ipsum lorem ipsum lorem ipsum<br>
      lorem ipsum lorem ipsum lorem ipsum<br>
      lorem ipsum lorem ipsum lorem ipsum<br>
      lorem ipsum
    </div>
    <div class="author-portrait" role="img" aria-label="Sylwetka autorki z profilu, dlon przy brodzie"></div>

    <p class="back-blurb first">
      ODLEGLE SCIEZKI NAUCZANIA, Zielone Mosty Pomiedzy Szkolami Zielone Mosty Pomiedzy Szkolami<br>
      ODLEGLE SCIEZKI NAUCZANIA, Zielone Mosty Pomiedzy Szkolami Zielone Mosty Pomiedzy Szkolami<br>
      ODLEGLE SCIEZKI NAUCZANIA, Zielone Mosty Pomiedzy Szkolami Zielone Mosty Pomiedzy Szkolami<br>
      ODLEGLE SCIEZKI NAUCZANIA, Zielone Mosty Pomiedzy Szkolami Zielone Mosty Pomiedzy Szkolami<br>
      ODLEGLE SCIEZKI NAUCZANIA, Zielone Mosty Pomiedzy Szkolami Zielone Mosty Pomiedzy Szkolami<br>
      ODLEGLE SCIEZKI NAUCZANIA, Zielone Mosty Pomiedzy Szkolami Zielone Mosty Pomiedzy Szkolami<br>
      ODLEGLE SCIEZKI NAUCZANIA, Zielone Mosty Pomiedzy Szkolami Zielone Mosty Pomiedzy Szkolami<br>
      ODLEGLE SCIEZKI NAUCZANIA, Zielone Mosty Pomiedzy Szkolami Zielone Mosty Pomiedzy Szkolami<br>
      ODLEGLE SCIEZKI NAUCZANIA, Zielone Mosty Pomiedzy Szkolami Zielone Mosty Pomiedzy Szkolami<br>
      ODLEGLE SCIEZKI NAUCZANIA, Zielone Mosty Pomiedzy Szkolami Zielone Mosty Pomiedzy Szkolami<br>
      ODLEGLE SCIEZKI NAUCZANIA, Zielone Mosty Pomiedzy Szkolami Zielone Mosty Pomiedzy Szkolami<br>
      ODLEGLE SCIEZKI NAUCZANIA, Zielone Mosty Pomiedzy Szkolami Zielone Mosty Pomiedzy Szkolami
    </p>
    <p class="back-blurb second">
      ODLEGLE SCIEZKI NAUCZANIA, Zielone Mosty Pomiedzy Szkolami Zielone Mosty Pomiedzy Szkolami<br>
      ODLEGLE SCIEZKI NAUCZANIA, Zielone Mosty Pomiedzy Szkolami Zielone Mosty Pomiedzy Szkolami<br>
      ODLEGLE SCIEZKI NAUCZANIA, Zielone Mosty Pomiedzy Szkolami Zielone Mosty Pomiedzy Szkolami<br>
      ODLEGLE SCIEZKI NAUCZANIA, Zielone Mosty Pomiedzy Szkolami Zielone Mosty Pomiedzy Szkolami<br>
      ODLEGLE SCIEZKI NAUCZANIA, Zielone Mosty Pomiedzy Szkolami Zielone Mosty Pomiedzy Szkolami<br>
      ODLEGLE SCIEZKI NAUCZANIA, Zielone Mosty Pomiedzy Szkolami Zielone Mosty Pomiedzy Szkolami<br>
      ODLEGLE SCIEZKI NAUCZANIA, Zielone Mosty Pomiedzy Szkolami Zielone Mosty Pomiedzy Szkolami<br>
      ODLEGLE SCIEZKI NAUCZANIA, Zielone Mosty Pomiedzy Szkolami Zielone Mosty Pomiedzy Szkolami<br>
      ODLEGLE SCIEZKI NAUCZANIA, Zielone Mosty Pomiedzy Szkolami Zielone Mosty Pomiedzy Szkolami<br>
      ODLEGLE SCIEZKI NAUCZANIA, Zielone Mosty Pomiedzy Szkolami Zielone Mosty Pomiedzy Szkolami<br>
      ODLEGLE SCIEZKI NAUCZANIA, Zielone Mosty Pomiedzy Szkolami Zielone Mosty Pomiedzy Szkolami<br>
      ODLEGLE SCIEZKI NAUCZANIA, Zielone Mosty Pomiedzy Szkolami Zielone Mosty Pomiedzy Szkolami
    </p>

    <div class="spine-text spine-author">Zofia Kradecka</div>
    <div class="spine-text spine-title">ODLEGLE SCIEZKI NAUCZANIA</div>

    <p class="front-author">Zofia Kradecka</p>
    <h1 class="front-title">ODLEGLE SCIEZKI<br>NAUCZANIA</h1>
    <p class="front-subtitle">Zielone Mosty Pomiedzy Szkolami Zielone Mosty Pomiedzy Szkolami</p>
  </section>

  <section class="inner-page" aria-label="Strona tytulowa">
    <p class="inner-author">Zofia Kradecka</p>
    <h2 class="inner-title">ODLEGLE SCIEZKI NAUCZANIA</h2>
    <p class="inner-subtitle">Zielone Mosty Pomiedzy Szkolami<br>Zielone Mosty Pomiedzy Szkolami</p>
    <svg class="inner-skyline" viewBox="0 0 346 100" width="346" height="100" preserveAspectRatio="none" role="img" aria-label="Szara ilustracja panoramy miasta z hotelem na trzech wiezach i diabelskim mlynem">
      <defs>
        <linearGradient id="skylineTone" x1="0" y1="0" x2="0" y2="1">
          <stop offset="0" stop-color="var(--page)"/>
          <stop offset="1" stop-color="var(--skyline)"/>
        </linearGradient>
      </defs>
      <rect x="0" y="0" width="346" height="100" fill="url(#skylineTone)"/>
    </svg>
  </section>

</main>
</body>
</html>
```